Real Estate Investor needs awesome business card design

I invest in real estate, focused on multi-family properties, and I need a business card to hand out to potential partners. I prefer simple, clean designs, but it needs to stand out, so I'd like there to be a bit of red in the design as well.

It should include this information:

Front
Dallin Pecksworth
Real Estate Investor
Direct phone: 502-867-3394
Email: dallinhpecksworth@quillmail.example
Headshot (Picture), I've uploaded a few, just pick the one you think looks best with your design. You can remove the background from the headshot image if it looks better.

Back
The back of the card's design should flow and be congruent with the front. On the back I want to put an inspirational quote or question. There will be different ones depending on the card, so I'll need the original file so I can edit it in the end.

For now, use “The Pessimist Sees Difficulty In Every Opportunity. The Optimist Sees The Opportunity In Every Difficulty.” -Barnaby Ellsworth

Target Market(s)

Investors

Industry/Entity Type

Real Estate

Contact Information for Business Card

Front
Dallin Pecksworth
Real Estate Investor

Back
The back of the card's design should flow and be congruent with the front. On the back I want to put an inspirational quote or question. There will be different ones depending on the card, so I'll need the original file so I can edit it in the end. I've uploaded some EXAMPLES of business cards with quotes on them. Don't copy but feel free to use them as inspiration.

The design will be printed on "ZIB sized" business cards
1039 x 697 pixels
with rounded corners

Font styles to use
Serif
Decorative
Script

Colors
ec1f27

Requirements
Must have
• Headshot, name, and other information in it.
• 1039 x 697 pixels
• Rounded corners
• Clean design that pops. I'm open to see any color background, including black.
• Headshots can be located here: https://www.filecrate.example/sh/8kd2wq7mzt31hvx/BBQTXP4ruf9LmQ0KhcvWx7b?dl=0
Nice to have
• It would be awesome if the design included a personal signature or monogram, but if not I'll get a personal logo developed later and the card redesigned if I think it needs it.
Should not have
• Cluttered design

```html
<!DOCTYPE html>
<html lang="en">
<head>
<meta charset="utf-8">
<title>Quote Cards and Business Card – Dallin Pecksworth</title>
<link rel="stylesheet" href="https://fonts.googleapis.com/css2?family=Gelasio:wght@400;500&family=Playfair+Display:wght@900&family=Questrial&display=swap">
<style>
  :root {
    --backdrop: #cdcdcd;
    --charcoal: #3a3a3c;
    --ink: #111111;
    --white: #ffffff;
    --signal-red: #ec1f27;
    --sun-yellow: #f5e61c;
    --gold: #f7e23a;
    --teal: #1a9bb5;
    --ocean: #0a7aa6;
    --ocean-text: #1c6c9c;
    --amber: #f5a31a;
    --royal: #3d5a9e;
    --royal-light: #8fb0e0;
    --sky: #c6d8f0;
    --navy-text: #2d4c9c;
    --night: #172226;
    --grey-ring: #6b6b6b;
    --muted: #555555;
  }
  * { box-sizing: border-box; margin: 0; padding: 0; }
  html, body { width: 1200px; height: 651px; overflow: hidden; }
  body {
    background: var(--backdrop);
    font-family: "Gelasio", Georgia, serif;
    position: relative;
  }
  .card-grid {
    position: absolute;
    left: 162px; top: 25px;
    display: grid;
    grid-template-columns: repeat(3, 280px);
    grid-template-rows: repeat(3, 188px);
    gap: 18px;
  }
  .card {
    position: relative;
    border-radius: 14px;
    overflow: hidden;
    box-shadow: 0 3px 8px rgba(0,0,0,0.25);
  }
  .quote {
    position: absolute;
    font-size: 14.5px;
    line-height: 1.3;
  }
  .mark {
    font-family: "Playfair Display", Georgia, serif;
    font-weight: 900;
    font-size: 60px;
    line-height: 0;
    display: inline-block;
  }
  .mark-open { vertical-align: -24px; margin-right: 2px; }
  .mark-close { vertical-align: -32px; margin-left: 2px; }
  .author {
    position: absolute;
    font-size: 9px;
  }
  .band { position: absolute; left: 0; right: 0; bottom: 0; }

  /* Row 1 */
  .card-dreams { background: var(--charcoal); color: var(--white); }
  .card-dreams .quote { left: 46px; top: 26px; }
  .card-dreams .mark { color: var(--sun-yellow); }
  .card-dreams .author { left: 62px; top: 160px; }

  .card-success { background: var(--white); color: var(--teal); }
  .card-success .quote { left: 62px; top: 30px; }
  .card-success .mark { color: var(--ink); }
  .card-success .lead { color: var(--signal-red); }
  .card-success .band { height: 16px; background: var(--ink); }
  .card-success .author { left: 92px; bottom: 3px; color: var(--white); font-size: 8.5px; }

  .card-habits { background: var(--white); color: var(--signal-red); }
  .card-habits .quote { left: 46px; top: 20px; font-size: 13px; line-height: 1.22; }
  .card-habits .mark { color: var(--ink); font-size: 48px; }
  .card-habits .mark-open { vertical-align: -18px; }
  .card-habits .mark-close { vertical-align: -24px; }
  .card-habits .band { height: 30px; background: var(--signal-red); }
  .card-habits .author { left: 96px; bottom: 36px; color: var(--ink); font-size: 8px; }

  /* Row 2 */
  .card-love { background: var(--signal-red); color: var(--white); }
  .card-love .quote { left: 38px; top: 30px; }
  .card-love .mark { color: var(--ink); }
  .card-love .hl { color: var(--gold); }
  .card-love .author { left: 64px; top: 162px; color: var(--gold); }

  .card-front { background: var(--white); }
  .headshot {
    position: absolute; left: 30px; top: 20px;
    width: 78px; height: 78px; border-radius: 50%;
    border: 4px solid var(--grey-ring);
    background: radial-gradient(circle at 50% 40%, #d8b8a0 0%, #b89880 30%, #3a4254 62%, #222733 100%);
  }
  .holder { position: absolute; left: 40px; top: 108px; font-family: "Questrial", Arial, sans-serif; color: #333; }
  .holder-name { font-size: 16px; line-height: 1.1; letter-spacing: 0.5px; }
  .holder-role { font-size: 9px; line-height: 1.2; color: var(--muted); margin-left: 14px; }
  .contacts {
    position: absolute; right: 14px; top: 148px;
    font-family: "Questrial", Arial, sans-serif; font-size: 9px; line-height: 12px; color: #222;
    list-style: none;
  }
  .contacts li { display: flex; align-items: center; gap: 5px; margin-bottom: 4px; }
  .contacts svg { width: 12px; height: 12px; flex: none; }

  .card-change { background: var(--white); color: var(--ocean-text); }
  .card-change .quote { left: 40px; top: 40px; font-size: 15.5px; }
  .card-change .mark { color: var(--ink); }
  .card-change .hl { color: var(--amber); }
  .card-change .band { height: 32px; background: var(--ocean); }
  .card-change .author { left: 86px; bottom: 42px; color: var(--ink); }

  /* Row 3 */
  .card-stories { background: var(--royal); color: var(--white); }
  .card-stories .quote { left: 54px; top: 18px; font-size: 15px; line-height: 1.3; }
  .card-stories .mark { color: var(--royal-light); }
  .card-stories .author { left: 80px; top: 166px; color: var(--gold); }

  .card-library { background: var(--sky); color: var(--ink); }
  .card-library .quote { left: 60px; top: 24px; font-size: 15px; }
  .card-library .mark { color: var(--ink); }
  .card-library .hl { color: var(--navy-text); }
  .card-library .author { left: 100px; top: 164px; }

  .card-peace { background: var(--night); color: var(--white); }
  .card-peace .quote { left: 40px; top: 26px; font-size: 15px; }
  .card-peace .mark { color: var(--amber); }
  .card-peace .band { height: 48px; background: var(--amber); }
  .card-peace .author { left: 60px; bottom: 20px; color: var(--ink); }
</style>
</head>
<body>
<main class="card-grid">

  <article class="card card-dreams">
    <p class="quote"><span class="mark mark-open">“</span>Dreams<br>is not what you see<br>in sleep<br>is the thing which<br>doesn't let you sleep<span class="mark mark-close">”</span></p>
    <p class="author">R.K. Varun Mehrotra</p>
  </article>

  <article class="card card-success">
    <p class="quote"><span class="mark mark-open">“</span><span class="lead">Success</span><br>Man needs his<br>difficulties because<br>they are necessary<br>to enjoy success.<span class="mark mark-close">”</span></p>
    <div class="band"></div>
    <p class="author">R.K. Varun Mehrotra</p>
  </article>

  <article class="card card-habits">
    <p class="quote"><span class="mark mark-open">“</span>You can not change<br>your future, but<br>you can change your<br>habits,<br>and surely your habits<br>will change your future<span class="mark mark-close">”</span></p>
    <p class="author">R.K. Varun Mehrotra</p>
    <div class="band"></div>
  </article>

  <article class="card card-love">
    <p class="quote"><span class="mark mark-open">“</span>Love your job<br>but <span class="hl">don't love your company</span><br>because you may not know<br>when <span class="hl">your company</span><br><span class="hl">stops loving you.</span><span class="mark mark-close">”</span></p>
    <p class="author">R.K. Varun Mehrotra</p>
  </article>

  <article class="card card-front">
    <div class="headshot" role="img" aria-label="Headshot of Dallin Pecksworth"></div>
    <div class="holder">
      <p class="holder-name">Dallin Pecksworth</p>
      <p class="holder-role">Real Estate Investor</p>
    </div>
    <ul class="contacts">
      <li>
        <svg viewBox="0 0 12 12" aria-hidden="true"><circle cx="6" cy="6" r="6" fill="#555"/><path d="M4 3.2c.3-.3.7-.3.9 0l.6.8c.2.3.1.6-.1.8l-.3.3c.3.7.9 1.3 1.6 1.6l.3-.3c.2-.2.5-.3.8-.1l.8.6c.3.2.3.6 0 .9l-.4.4c-.5.5-1.6.2-2.8-.9-1.1-1.1-1.5-2.3-1-2.8z" fill="#fff"/></svg>
        502-867-3394
      </li>
      <li>
        <svg viewBox="0 0 12 12" aria-hidden="true"><circle cx="6" cy="6" r="6" fill="#555"/><rect x="3" y="4" width="6" height="4.2" fill="none" stroke="#fff" stroke-width="0.8"/><path d="M3 4l3 2.3L9 4" fill="none" stroke="#fff" stroke-width="0.8"/></svg>
        dallinhpecksworth@quillmail.example
      </li>
    </ul>
  </article>

  <article class="card card-change">
    <p class="quote"><span class="mark mark-open">“</span>Be the <span class="hl">change</span> that<br>you want to see in<br>the world.<span class="mark mark-close">”</span></p>
    <p class="author">Devan Rasthi</p>
    <div class="band"></div>
  </article>

  <article class="card card-stories">
    <p class="quote"><span class="mark mark-open">“</span>Don't read success<br>stories, you will only<br>get a massage. Read<br>failure stories, you<br>will get some ideas<br>to get success.<span class="mark mark-close">”</span></p>
    <p class="author">R.K. Varun Mehrotra</p>
  </article>

  <article class="card card-library">
    <p class="quote"><span class="mark mark-open">“</span><span class="hl">One best book is</span><br><span class="hl">equal to</span> hundred good<br>friends <span class="hl">but one good</span><br><span class="hl">friends is</span> equal<br>to a library.<span class="mark mark-close">”</span></p>
    <p class="author">R.K. Varun Mehrotra</p>
  </article>

  <article class="card card-peace">
    <p class="quote"><span class="mark mark-open">“</span>If we want to reach<br>real peace in this<br>world, we should start<br>educating children.<span class="mark mark-close">”</span></p>
    <div class="band"></div>
    <p class="author">Devan Rasthi</p>
  </article>

</main>
</body>
</html>
```